artist "stamp" design

Im a young artist. I`m making a stamp with my information so i can make homemade business cards, so I need the following information to look good together and simple to read:

Lorena Batalla Quiroga

www.lorebtqz.com

lorenabq47@fotmail.example

i want a very clan look, but with some personality. a simple logo or "look" would be great but nothing to fancy.

An idea I had was to make it look like it was written with a typewriter or a concept like that...be creative! thank you!
Updates

I don't want any image or icon, just letters, I need it to be compacto, I'm making a stamp

I don't want it to say photography 

I dont want my name to take over so it should stay close to the size as the rest of the info.

all my info should be included, this is not a logo its a design for a stamp meant to fin in a business card.

Target Market(s)

I'm a photographer, I want something very simple and I need this to make a stamp that ill use to pit on my cards and CV. I want something simple and modern

Industry/Entity Type

Business

Logo Text

Lorena Batalla Quiroga

Logo styles of interest
Abstract Logo
Wordmark Logo
Lettermark Logo
Font styles to use
Serif
Sans Serif

Requirements
Must have
• Has to look young and fresh
Nice to have
• Have to see how it looks on a business card with website and and email
Should not have
• Images

```html
<!DOCTYPE html>
<html lang="en">
<head>
<meta charset="UTF-8">
<title>Lorena Batalla Quiroga — Stamp</title>
<link rel="stylesheet" href="https://fonts.googleapis.com/css2?family=Pacifico&display=swap">
<style>
  :root {
    --paper: #ffffff;
    --ink: #1c1c1c;
  }
  html, body {
    margin: 0;
    padding: 0;
    overflow: hidden;
    background: var(--paper);
  }
  .canvas {
    width: 942px;
    height: 1200px;
    position: relative;
    overflow: hidden;
    background: var(--paper);
    display: flex;
    align-items: center;
    justify-content: center;
  }
  .stamp {
    display: flex;
    flex-direction: column;
    align-items: center;
    gap: 92px;
    color: var(--ink);
    font-family: "Pacifico", cursive;
    font-weight: 400;
    line-height: 1;
    text-align: center;
  }
  .stamp__name {
    margin: 0;
    font-size: 58px;
    font-weight: 400;
    letter-spacing: 0.5px;
  }
  .stamp__web {
    margin: 0;
    font-size: 52px;
  }
  .stamp__email {
    margin: 0;
    font-size: 48px;
  }
</style>
</head>
<body>
  <main class="canvas">
    <section class="stamp">
      <h1 class="stamp__name">Lorena Batalla Quiroga</h1>
      <p class="stamp__web">www.lorebtqz.com</p>
      <p class="stamp__email">lorenabq47@fotmail.example</p>
    </section>
  </main>
</body>
</html>
```